Pwrpt Describing Grant Attributes

We recently won a grant to deliver services to students with disabilities. I need a PowerPoint presentation to explain the grant to stakeholders. The PowerPoint should summarize the key attributes of the grant in a way that can be shared with anyone. I am attaching the entire Narrative, an abstract, a summary of the grant, and Measures that have to be obtained.

Target Market(s)

Educators

Requirements
Must have
• Use the Colors from our website: https://k7v.org/
Nice to have
• where can use https://infohub.bkt.office.xq.us/ for any additional information

```html
<!DOCTYPE html>
<html lang="en">
<head>
<meta charset="utf-8">
<title>Stepwise Futures – Grant Summary Deck</title>
<link href="https://fonts.googleapis.com/css2?family=Lexend:wght@300;400;500&family=Inter:wght@400;500&display=swap" rel="stylesheet">
<style>
  :root{
    --board:#a8a8a8;
    --paper:#ffffff;
    --paper-soft:#f3f3f3;
    --ink:#1e1e1e;
    --ink-soft:#4a4a4a;
    --orange:#f26f21;
    --orange-deep:#ee6a1c;
    --yellow:#f6b41b;
    --teal:#1d6c87;
  }
  *{box-sizing:border-box;margin:0;padding:0}
  html,body{width:1200px;height:411px;overflow:hidden}
  body{background:var(--board);position:relative;font-family:"Inter",Arial,sans-serif;color:var(--ink)}
  .slide{position:absolute;width:266px;height:149px;overflow:hidden;background:linear-gradient(135deg,var(--paper) 0%,var(--paper-soft) 100%);box-shadow:0 2px 6px rgba(0,0,0,.18)}
  .heading{font-family:"Lexend",Arial,sans-serif;font-weight:400;letter-spacing:.08em;color:var(--ink)}
  .body-copy{font-size:3.1px;line-height:1.9;color:var(--ink-soft)}
  .brand-tag{position:absolute;display:flex;align-items:center;gap:2px;font-family:"Lexend",Arial,sans-serif;font-weight:500;font-size:3.6px;color:var(--ink);letter-spacing:.02em;white-space:nowrap}
  .brand-tag .dot{width:6px;height:6px;border-radius:50%;background:var(--orange)}
  .photo{position:absolute}

  /* cover */
  .cover{left:46.6px;top:45px}
  .cover .brand-tag{left:13px;top:27px;font-size:5.3px}
  .cover .brand-tag .dot{width:10px;height:10px}
  .cover-title{position:absolute;left:12px;top:44px;font-size:18px;line-height:1.2;letter-spacing:.05em;font-weight:500}
  .cover-sub{position:absolute;left:13px;top:92px;font-family:"Lexend",Arial,sans-serif;font-size:4.4px;line-height:1.7;letter-spacing:.05em}
  .cover-date{position:absolute;left:12px;top:113px;background:var(--yellow);color:var(--ink);font-family:"Lexend",Arial,sans-serif;font-size:5px;padding:2.5px 10px;border-radius:6px}
  .cover-art{position:absolute;left:133px;top:0;width:133px;height:149px}

  /* intro */
  .intro{left:328.5px;top:45px}
  .intro .brand-tag,.objectives .brand-tag,.need .brand-tag{right:6px;top:6px}
  .intro-frame{position:absolute;left:18px;top:40px;width:80px;height:76px;border:1px solid var(--orange);border-radius:7px}
  .intro-photo-a{left:35px;top:25px;width:73px;height:64px;border-radius:6px;background:linear-gradient(160deg,#6d5a48,#b29a80 60%,#d9cdbd)}
  .intro-photo-b{left:9px;top:57px;width:76px;height:68px;border-radius:6px;background:linear-gradient(150deg,#c9c3bb,#9a6f5b 55%,#4f4a52)}
  .intro-rule{position:absolute;left:118px;top:22px;width:.6px;height:110px;background:var(--orange)}
  .intro-title{position:absolute;left:128px;top:26px;font-size:10px}
  .intro-text{position:absolute;left:128px;top:41px;width:128px}
  .intro-sub{position:absolute;left:128px;top:96px;font-size:4.6px;letter-spacing:.06em}
  .intro-target{position:absolute;left:128px;top:104px;width:128px}

  /* objectives */
  .objectives{left:608.5px;top:45px}
  .obj-title{position:absolute;left:10px;top:8px;font-size:8.5px;line-height:1.25}
  .obj-lead{position:absolute;left:11px;top:33px;font-family:"Lexend",Arial,sans-serif;font-size:3.6px;line-height:1.6;color:var(--orange);letter-spacing:.06em}
  .obj-list{position:absolute;left:11px;top:47px;width:140px;list-style:none}
  .obj-list li{position:relative;padding-left:4px;font-size:2.6px;line-height:1.7;color:var(--ink-soft);margin-bottom:2.6px}
  .obj-list li::before{content:"";position:absolute;left:0;top:1.3px;width:1.8px;height:1.8px;border-radius:50%;background:var(--yellow)}
  .obj-photo{left:161px;top:22px;width:94px;height:114px;border-radius:7px;background:linear-gradient(170deg,#d9d2c4 0%,#8e7c62 45%,#5b4a3d 100%)}

  /* need */
  .need{left:888px;top:45px}
  .need-title{position:absolute;left:10px;top:16px;font-size:9.5px}
  .need-screen{position:absolute;left:20px;top:47px;width:118px;height:72px;background:#1b1b1b;border-radius:4px 4px 0 0;padding:3px}
  .need-screen .photo{position:relative;width:100%;height:100%;background:linear-gradient(120deg,#6e4c36,#c2a36a 50%,#f0d64a 70%,#5c4637)}
  .need-base{position:absolute;left:5px;top:119px;width:148px;height:3px;background:#2a2a2a;border-radius:0 0 3px 3px}
  .need-text{position:absolute;left:150px;top:27px;width:108px;height:110px;overflow:hidden}
  .need-text p+p{margin-top:4px}

  /* challenges */
  .challenges{left:131.4px;top:216.7px}
  .challenges-panel{position:absolute;left:0;top:0;width:94px;height:149px;background:var(--teal);padding:9px 8px}
  .challenges-title{font-size:8.2px;line-height:1.25;color:#fff;letter-spacing:.05em}
  .challenges-panel .body-copy{color:#e8f0f3;font-size:2.8px;margin-top:6px}
  .challenges-panel .body-copy+.body-copy{margin-top:4px}
  .challenges-photo{left:94px;top:0;width:172px;height:149px;background:linear-gradient(120deg,#3d5566 0%,#7d8e98 40%,#c9b7a4 65%,#5d6f7d 100%)}
  .challenges .brand-tag{right:6px;top:7px;color:#fff}

  /* thanks */
  .thanks{left:413.3px;top:216.7px;background:linear-gradient(180deg,var(--yellow) 0%,#f49a1f 50%,var(--orange-deep) 100%)}
  .thanks-mark{position:absolute;left:30px;top:38px;width:80px;text-align:center;color:#fff}
  .thanks-mark .circle{width:32px;height:32px;border-radius:50%;border:2.4px solid #fff;margin:0 auto 6px}
  .thanks-mark .name{font-family:"Lexend",Arial,sans-serif;font-size:8.2px;font-weight:500;white-space:nowrap;margin-left:-20px;margin-right:-20px}
  .socials{display:flex;justify-content:center;gap:3px;margin-top:8px}
  .socials span{width:7px;height:7px;border:.6px solid #fff;border-radius:50%}
  .thanks-rule{position:absolute;left:143px;top:38px;width:.6px;height:75px;background:#fff}
  .thanks-title{position:absolute;left:155px;top:44px;font-size:13px;color:#fff}
  .contact{position:absolute;left:155px;top:66px;list-style:none;color:#fff;font-size:3.7px;line-height:1.6}
  .contact li{display:flex;gap:4px;margin-bottom:4px}
  .contact svg{width:4px;height:4px;flex:none;margin-top:.6px}

  /* brand lockup */
  .lockup{position:absolute;left:787px;top:260px;display:flex;align-items:center;gap:8px}
  .lockup .circle{width:46px;height:46px;border-radius:50%;background:var(--orange)}
  .lockup .name{font-family:"Lexend",Arial,sans-serif;font-weight:500;font-size:21px;color:#2b2b2b;letter-spacing:.01em}
</style>
</head>
<body>

<section class="slide cover">
  <div class="brand-tag"><span class="dot"></span>STEPWISE FUTURES</div>
  <h1 class="heading cover-title">STEPWISE<br>FUTURES</h1>
  <p class="cover-sub">Summary of the Career Link in Northvale<br>(CLiNV) Federal Grant Proposal</p>
  <span class="cover-date">April 2024</span>
  <svg class="cover-art" viewBox="0 0 133 149" role="img" aria-label="Photo collage of students studying in warm orange and yellow light">
    <defs>
      <linearGradient id="artTop" x1="0" y1="0" x2="1" y2="1"><stop offset="0" stop-color="#c9571b"/><stop offset="1" stop-color="#f08a25"/></linearGradient>
      <linearGradient id="artBottom" x1="0" y1="0" x2="1" y2="1"><stop offset="0" stop-color="#d2651c"/><stop offset="1" stop-color="#f2b51c"/></linearGradient>
    </defs>
    <path d="M0 0H128C95 20 60 50 10 70 4 60 0 45 0 30Z" fill="url(#artTop)"/>
    <path d="M133 20V149H120C100 120 60 100 30 90 75 70 110 45 133 20Z" fill="#f4c22a"/>
    <path d="M6 95C40 100 85 125 110 149H4C3 130 4 110 6 95Z" fill="url(#artBottom)"/>
  </svg>
</section>

<section class="slide intro">
  <div class="brand-tag"><span class="dot"></span>STEPWISE FUTURES</div>
  <div class="intro-frame"></div>
  <div class="photo intro-photo-a" role="img" aria-label="Photo of a teacher in a classroom"></div>
  <div class="photo intro-photo-b" role="img" aria-label="Photo of students working together at a computer"></div>
  <div class="intro-rule"></div>
  <h2 class="heading intro-title">INTRODUCTION</h2>
  <p class="body-copy intro-text">In partnership with the Northvale Public Education Department, Stepwise Futures (SWF) seeks to transform career-connected learning (CCL) opportunities for students with disabilities. The Career Link in Northvale (CLiNV) grant represents an initiative to establish a shared vision and foster partnerships across sectors, providing comprehensive support services to help these students successfully transition into postsecondary programs and competitive integrated employment (CIE).</p>
  <h3 class="heading intro-sub">Target Population</h3>
  <p class="body-copy intro-target">CLiNV will cater to students with disabilities across all districts throughout Northvale, focusing mainly in areas where a significant number of Hispanic students reside.</p>
</section>

<section class="slide objectives">
  <div class="brand-tag"><span class="dot"></span>STEPWISE FUTURES</div>
  <h2 class="heading obj-title">Project Objectives and<br>Outcomes</h2>
  <p class="obj-lead">The objectives and intended outcomes of this project<br>for students with disabilities are as follows</p>
  <ul class="obj-list">
    <li>Relevant CCL Content: Aligning course material with the workforce requirements in Northvale.</li>
    <li>Enhanced Access to Career Exploration: Ensuring that students with disabilities have access and tools that facilitate career exploration, aiding their transition from school.</li>
    <li>Improved Math Proficiency and Motivation: Enhancing students' mathematical skills and motivation levels to better prepare them for an evolving job market.</li>
    <li>Fostering Self-Awareness and Advocacy: Empowering students with disabilities to build self-confidence and advocate for themselves.</li>
    <li>Enhancing Teacher and Partner Training: Equipping K-12 teachers and partners with the knowledge and skills to support the career journeys of students with disabilities.</li>
    <li>Building a Unified Vision: Demonstrating the power of a shared vision (CCL) to connect educators, businesses, community stakeholders, and state-level agencies.</li>
    <li>Improving Measurement of CCL in Special Education: Developing systems for collecting data that accurately measure growth in CCL awareness and proficiency.</li>
  </ul>
  <div class="photo obj-photo" role="img" aria-label="Photo of an audience seated at a conference presentation"></div>
</section>

<section class="slide need">
  <div class="brand-tag"><span class="dot"></span>STEPWISE FUTURES</div>
  <h2 class="heading need-title">Magnitude Of The Need</h2>
  <div class="need-screen"><div class="photo" role="img" aria-label="Photo of a student holding books in a library, shown on a laptop screen"></div></div>
  <div class="need-base"></div>
  <div class="need-text body-copy">
    <p>Two major trends in education today are increasingly influencing school priorities and programs. The first is relevance through a career lens: Schools need to increase their focus on preparing students for postsecondary education options and for work. The second is partnerships: Schools cannot accomplish many of its initiatives for improving student outcomes, particularly in special education, without multi-sector public and private partnerships, resources, and support. Bringing schools and community partners together can produce cooperative career-focused programs that align the realities of the workplace with what students learn in school. When applied to special education, we need "all hands on deck."</p>
    <p>The proposed CLiNV project introduces Career-Connected Learning (CCL) to special education and as a shared unifying vision across the project's partnership collaboration. CCL has been shown to be a successful model for increasing student motivation and engagement by making career exploration and development a core approach to learning. And yet, to date, no implementation of CCL has been adapted for students with disabilities, who also need to prepare for next steps following high-school.</p>
  </div>
</section>

<section class="slide challenges">
  <div class="challenges-panel">
    <h2 class="heading challenges-title">Challenges to<br>Equitable Acces</h2>
    <p class="body-copy">Schools face many challenges to ensuring equitable access for students with disabilities. Some of these challenges include inadequate program design and accommodations to help students with disabilities participate; lack of resources in rural areas, which complicates learning; the need for specialized, ongoing training for teachers and community partners working with this population; and identification of business mentors who can help prepare these students for work by sharing what they do at work.</p>
    <p class="body-copy">Teacher shortages across the state (and the nation) are particularly hard-felt in rural regions of Northvale, which makes up roughly one-third of the population of the state. This challenge is being addressed through incentives and outreach to attract teachers to these areas.</p>
  </div>
  <div class="photo challenges-photo" role="img" aria-label="Photo of a smiling student studying at a laptop"></div>
  <div class="brand-tag"><span class="dot"></span>STEPWISE FUTURES</div>
</section>

<section class="slide thanks">
  <div class="thanks-mark">
    <div class="circle"></div>
    <div class="name">STEPWISE FUTURES</div>
    <div class="socials"><span></span><span></span><span></span><span></span></div>
  </div>
  <div class="thanks-rule"></div>
  <h2 class="heading thanks-title">Thank You</h2>
  <ul class="contact">
    <li><svg viewBox="0 0 10 10"><path d="M5 0a3.5 3.5 0 0 0-3.5 3.5C1.5 6 5 10 5 10s3.5-4 3.5-6.5A3.5 3.5 0 0 0 5 0Zm0 5a1.5 1.5 0 1 1 0-3 1.5 1.5 0 0 1 0 3Z" fill="#fff"/></svg><span>418 Alder Lane, Suite 12<br>Fairview, ST 00000</span></li>
    <li><svg viewBox="0 0 10 10"><path d="M2 0 4 2.5 3 4c.8 1.4 1.6 2.2 3 3l1.5-1L10 8l-1.5 2C4 10 0 6 0 1.5Z" fill="#fff"/></svg><span>800.555.0142</span></li>
    <li><svg viewBox="0 0 10 10"><path d="M0 2h10v6H0Zm0 0 5 3.5L10 2" fill="#fff" stroke="#f39a23" stroke-width=".8"/></svg><span>hello@k7v.org</span></li>
  </ul>
</section>

<div class="lockup">
  <span class="circle"></span>
  <span class="name">STEPWISE FUTURES</span>
</div>

</body>
</html>
```